New Automotive supply business in need of label designs for additive range

I need front and back label design for about 12 different variety of products. They are all to do with the Automotive additive industry such as Petrol injector cleaner, Engine Flush, Oil treatments etc. I will provide overall measurements of the label in the brief as well as examples of artwork that I like. Label must comply with local regulations, i can assist you with this. We will start with one product only, and if successful I am happy to hire you to do the remainder of the project. I would like to see designs that use my company logo colors. These products are for the workshop industry only (not retail) so does not have to be too animated.You will see my logo designs under the name "kalmor" in the uploaded files.Product Name is : Motor Prime & Renew
Front Label must say:PREPARES ENGINES FOR NEW OIL
RESTORES COMPRESSION
MINIMISES CONTAMINATION WITH NEW OIL
CONTAINS KALMOR TUFFLINE PROTECTION
RECOMMENDED FOR PETROL, DIESEL AND HYBRID ENGINES
350ML
Dimensions of metal can that will be used for label is : 175mm in height and 56mm in diameter. IN THE UPLOADED FILES YOU WILL SEE A SAMPLE OF THE ACTUAL CAN TO BE USED.
I have now included an example of a shield/guard that should be shown on the rear of the label if possible, im happy if you come up with your own shield designs.

Target Market(s)

Mechanics

Industry/Entity Type

Automotive Part

Requirements
Must have
• My logo on top
Nice to have
• Silver background
Should not have
• Pictures of engines or engine parts etc

```html
<!DOCTYPE html>
<html lang="en">
<head>
<meta charset="utf-8">
<title>Kalmor Motor Prime and Renew – Front Label</title>
<link rel="stylesheet" href="https://fonts.googleapis.com/css2?family=Open+Sans:wght@400;600;700&family=Russo+One&display=swap">
<style>
  :root {
    --page: #ffffff;
    --copper-dark: #5e2c22;
    --copper: #b4451f;
    --copper-bright: #f05a22;
    --silver-dark: #5d5f66;
    --silver-mid: #a9abb0;
    --silver-light: #f4f4f5;
    --navy: #1c2f5e;
    --ink: #141414;
    --white: #ffffff;
    --accent-orange: #f26522;
  }
  html, body {
    margin: 0;
    padding: 0;
    width: 1200px;
    height: 1200px;
    overflow: hidden;
    background: var(--page);
  }
  .canvas {
    position: relative;
    width: 1200px;
    height: 1200px;
  }
  .label {
    position: absolute;
    left: 423px;
    top: 47px;
    width: 354px;
    height: 1105px;
    display: block;
  }
  .brand-name {
    font-family: "Open Sans", sans-serif;
    font-weight: 700;
    font-size: 38px;
    fill: var(--silver-light);
    letter-spacing: 2px;
  }
  .brand-tagline {
    font-family: "Open Sans", sans-serif;
    font-weight: 600;
    font-size: 10px;
    fill: var(--white);
    letter-spacing: 0.6px;
  }
  .product-title {
    font-family: "Russo One", sans-serif;
    fill: var(--silver-light);
    font-style: italic;
  }
  .benefit {
    font-family: "Open Sans", sans-serif;
    font-weight: 600;
    font-size: 14px;
    fill: var(--ink);
  }
  .volume {
    font-family: "Open Sans", sans-serif;
    font-weight: 700;
    font-size: 27px;
    fill: var(--white);
  }
  .volume-unit { font-size: 19px; }
  .footer-line {
    font-family: "Open Sans", sans-serif;
    font-weight: 400;
    font-size: 19px;
    fill: var(--white);
  }
</style>
</head>
<body>
<main class="canvas">
  <svg class="label" viewBox="0 0 354 1105" xmlns="http://www.w3.org/2000/svg" aria-label="Kalmor Motor Prime and Renew front label">
    <defs>
      <linearGradient id="copperSheen" x1="0" y1="0" x2="1" y2="0">
        <stop offset="0" stop-color="var(--copper-dark)"/>
        <stop offset="0.3" stop-color="var(--copper)"/>
        <stop offset="0.5" stop-color="var(--copper-bright)"/>
        <stop offset="0.7" stop-color="var(--copper)"/>
        <stop offset="1" stop-color="var(--copper-dark)"/>
      </linearGradient>
      <linearGradient id="silverSheen" x1="0" y1="0" x2="1" y2="0">
        <stop offset="0" stop-color="var(--silver-dark)"/>
        <stop offset="0.25" stop-color="var(--silver-mid)"/>
        <stop offset="0.5" stop-color="var(--silver-light)"/>
        <stop offset="0.75" stop-color="var(--silver-mid)"/>
        <stop offset="1" stop-color="var(--silver-dark)"/>
      </linearGradient>
      <linearGradient id="badgeFill" x1="0" y1="0" x2="1" y2="0">
        <stop offset="0" stop-color="var(--copper)"/>
        <stop offset="0.5" stop-color="var(--copper-bright)"/>
        <stop offset="1" stop-color="var(--copper)"/>
      </linearGradient>
    </defs>

    <rect class="body-copper" x="0" y="0" width="354" height="1105" fill="url(#copperSheen)"/>

    <g class="brand">
      <circle cx="53" cy="232" r="10" fill="var(--silver-light)"/>
      <text class="brand-name" x="185" y="246" text-anchor="middle">KALMOR</text>
      <line x1="73" y1="262" x2="118" y2="262" stroke="var(--accent-orange)" stroke-width="1.5"/>
      <line x1="236" y1="262" x2="281" y2="262" stroke="var(--accent-orange)" stroke-width="1.5"/>
      <text class="brand-tagline" x="177" y="265" text-anchor="middle">DRIVE WITH KALMOR</text>
    </g>

    <polygon class="panel-silver" points="177,309 354,373 354,941 177,1005 0,941 0,373" fill="url(#silverSheen)"/>

    <g class="product-badge">
      <polygon points="177,375 287,395 309,455 287,515 177,536 67,515 44,455 67,395" fill="url(#badgeFill)" stroke="var(--navy)" stroke-width="4" stroke-linejoin="round"/>
      <text class="product-title" x="177" y="425" text-anchor="middle" font-size="27">Motor Prime</text>
      <text class="product-title" x="177" y="463" text-anchor="middle" font-size="23">and</text>
      <text class="product-title" x="177" y="503" text-anchor="middle" font-size="29">Renew</text>
    </g>

    <g class="benefits">
      <g class="bullet" fill="var(--accent-orange)">
        <circle cx="32" cy="629" r="8"/>
        <circle cx="32" cy="694" r="8"/>
        <circle cx="32" cy="759" r="8"/>
        <circle cx="32" cy="823" r="8"/>
        <circle cx="32" cy="888" r="8"/>
      </g>
      <text class="benefit" x="64" y="634">PREPARES ENGINES FOR NEW OIL</text>
      <text class="benefit" x="64" y="699">RESTORES COMPRESSION</text>
      <text class="benefit" x="64" y="744">MINIMISES CONTAMINATION</text>
      <text class="benefit" x="64" y="764">WITH NEW OIL</text>
      <text class="benefit" x="64" y="809">CONTAINS KALMOR TUFFLINE</text>
      <text class="benefit" x="64" y="829">PROTECTION</text>
      <text class="benefit" x="64" y="874">RECOMMENDED FOR PETROL,</text>
      <text class="benefit" x="64" y="894">DIESEL AND HYBRID ENGINES</text>
    </g>

    <text class="volume" x="177" y="1056" text-anchor="middle">350<tspan class="volume-unit">ML</tspan></text>
    <text class="footer-line" x="177" y="1091" text-anchor="middle">Drive with KALMOR</text>
  </svg>
</main>
</body>
</html>
```